Service Level Agreement

Details for my new Brochure Design Project will be added soon,

I have attached a couple of documents that I would like to show that have information I want to show and https://www.oru-lanex.example Is my website,

Document show old business address new one is below:
ORU LANEX LTD
Marlow Court,
Fenwick street
Dunhollow
ZX4 7QN

Target Market(s)

Education

Requirements
Must have
• Different options of prices shown on the attached document.

```html
<!DOCTYPE html>
<html lang="en">
<head>
<meta charset="utf-8">
<title>ORU LANEX – Service Level Agreement Brochure</title>
<link rel="stylesheet" href="https://fonts.googleapis.com/css2?family=Montserrat:wght@300;400;600;700;800&family=Open+Sans:wght@400;600;700&display=swap">
<style>
:root{
  --navy:#2b4a7e;
  --navy-deep:#1b2f57;
  --navy-gap:#22396a;
  --orange:#f0885a;
  --orange-text:#ef7a43;
  --paper:#fbfbfb;
  --stage:#e2e3e5;
  --ink:#3a3f4a;
  --teal:#3fb4d6;
}
*{box-sizing:border-box;margin:0;padding:0}
html,body{width:1200px;height:2695px;overflow:hidden}
body{background:var(--stage);font-family:"Open Sans",sans-serif;color:var(--ink);position:relative}
.section{position:absolute;left:0;width:1200px;height:898px}
.section--front{top:0}
.section--spread{top:898px;background:#e6e7e9}
.section--inside{top:1797px;background:#e4e5e7}

/* ---------- front cover ---------- */
.cover{position:relative;width:537px;height:760px;background:var(--paper);overflow:hidden;box-shadow:0 18px 40px rgba(0,0,0,.18)}
.cover__circuit{position:absolute;left:0;top:0;width:537px;height:540px;background:radial-gradient(circle at 45% 55%,#3a64a3 0,var(--navy) 45%,var(--navy-deep) 100%)}
.cover__brand{position:absolute;left:34px;top:38px;color:#fff}
.brand-name{font-family:"Montserrat",sans-serif;font-weight:700;letter-spacing:2px;font-size:30px;display:flex;align-items:center;gap:10px}
.brand-name .mark{width:16px;height:16px;background:var(--orange)}
.brand-tag{font-family:"Montserrat",sans-serif;font-size:9.5px;letter-spacing:1.6px;margin-top:4px}
.tile{position:absolute;overflow:hidden}
.tile--photo-desk{left:363px;top:0;width:174px;height:92px;background:linear-gradient(135deg,#d9d3cc,#7a6f68 60%,#2f3a4c)}
.tile--it{left:363px;top:98px;width:174px;height:172px;background:var(--orange)}
.tile--photo-board{left:363px;top:276px;width:174px;height:264px;background:linear-gradient(160deg,#e0b24a,#a87a2a 40%,#3a4a66 75%,#1e2a42)}
.tile--curriculum{left:0;top:370px;width:174px;height:170px;background:var(--orange)}
.tile--hardware{left:180px;top:370px;width:177px;height:170px;background:var(--orange)}
.tile__icon{position:absolute;left:50%;top:36px;transform:translateX(-50%)}
.tile__label{position:absolute;left:0;right:0;bottom:22px;text-align:center;color:#fff;font-family:"Montserrat",sans-serif;font-size:12px;line-height:1.2;letter-spacing:1px}
.tile__label b{font-weight:700}
.cover__title{position:absolute;left:0;right:0;top:575px;text-align:center;font-family:"Montserrat",sans-serif}
.title-light{font-weight:400;font-size:38px;color:var(--navy);letter-spacing:1px}
.title-bold{font-weight:800;font-size:42px;color:var(--orange-text);letter-spacing:1px;margin-top:-4px}
.ribbon{display:inline-block;margin-top:10px;background:var(--navy);color:#fff;font-weight:700;font-size:15px;padding:6px 34px;clip-path:polygon(0 0,100% 0,96% 50%,100% 100%,0 100%,4% 50%)}

/* ---------- back cover ---------- */
.back{position:relative;width:537px;height:760px;background:linear-gradient(160deg,#2a4a80,var(--navy-deep) 70%);overflow:hidden}
.back__strip{position:absolute;right:0;top:0;width:150px;height:760px;background:linear-gradient(180deg,#7fdcf0 0,var(--teal) 25%,#1d6f8f 55%,#0f3550 100%)}
.back__info{position:absolute;left:64px;top:500px;color:#fff;font-size:10px;line-height:1.45}
.back__info .brand-name{font-size:18px;letter-spacing:1.5px}
.back__info .brand-tag{font-size:6px;margin-bottom:10px}
.contact-head{color:var(--orange-text);font-family:"Montserrat",sans-serif;font-weight:700;font-size:11px;margin:14px 0 4px}

/* ---------- scaled spread ---------- */
.spread{position:absolute;left:230px;top:186px;width:740px;height:523px;display:flex;box-shadow:0 18px 40px rgba(0,0,0,.2)}
.spread__page{width:370px;height:523px;overflow:hidden;position:relative}
.spread__page > *{transform:scale(.689);transform-origin:0 0;box-shadow:none}

/* ---------- inside pages ---------- */
.inside{position:absolute;left:180px;top:152px;width:840px;height:594px;display:flex;box-shadow:0 18px 40px rgba(0,0,0,.18)}
.page{position:relative;width:420px;height:594px;background:var(--paper);padding:26px 30px 40px;overflow:hidden;font-size:7.2px;line-height:1.45}
.page--left{border-right:1px solid #d6d7da}
.page__note{text-align:center;font-weight:700;font-size:7.5px;color:var(--navy);padding-bottom:6px;border-bottom:1px solid #cfd3da;margin-bottom:10px}
.h{font-family:"Montserrat",sans-serif;font-weight:700;font-size:8.6px;color:var(--navy);margin:9px 0 4px;text-transform:uppercase}
.h span{color:var(--orange-text)}
.ticks{list-style:none}
.ticks li{position:relative;padding-left:11px;margin-bottom:2px}
.ticks li::before{content:"";position:absolute;left:0;top:2px;width:6px;height:6px;border-radius:50%;background:var(--navy)}
.cols{display:grid;grid-template-columns:repeat(3,1fr);gap:0 10px}
.cols--2{grid-template-columns:1fr 1fr}
.page p{margin-bottom:3px}
.page__foot{position:absolute;left:30px;right:30px;bottom:14px;display:flex;justify-content:space-between;align-items:center}
.foot-brand{font-family:"Montserrat",sans-serif;font-weight:700;font-size:9px;color:var(--navy);letter-spacing:1px}
.foot-web{background:var(--navy);color:#fff;font-weight:700;font-size:7px;padding:3px 10px}
.price b{color:var(--navy)}
</style>
</head>
<body>

<!-- Front cover -->
<section class="section section--front">
  <div class="cover" style="position:absolute;left:331px;top:69px">
    <div class="cover__circuit" role="img" aria-label="Blue circuit board pattern with glowing hexagons"></div>
    <div class="cover__brand">
      <div class="brand-name"><span class="mark"></span>ORU LANEX</div>
      <div class="brand-tag">EDUCATION SUPPORT &amp; INSTALLATION</div>
    </div>
    <div class="tile tile--photo-desk" role="img" aria-label="Photo of a technician working on computer hardware"></div>
    <div class="tile tile--it">
      <svg class="tile__icon" width="62" height="62" viewBox="0 0 62 62" fill="none" stroke="#fff" stroke-width="2.4"><circle cx="31" cy="26" r="11"/><path d="M31 9v5M31 38v5M14 26h5M43 26h5M19 14l4 4M39 34l4 4M43 14l-4 4M23 34l-4 4"/><path d="M8 50c8-6 14-6 22-2h10c4 0 4 5 0 5H27M8 56h30l14-8"/></svg>
      <div class="tile__label">IT <b>SUPPORT</b></div>
    </div>
    <div class="tile tile--photo-board" role="img" aria-label="Close-up photo of a computer motherboard"></div>
    <div class="tile tile--curriculum">
      <svg class="tile__icon" width="66" height="62" viewBox="0 0 66 62" fill="none" stroke="#fff" stroke-width="2.4"><path d="M16 34a10 10 0 0 1 2-20 14 14 0 0 1 27 2 9 9 0 0 1 3 18z"/><path d="M22 34v14M33 34v20M44 34v12"/><circle cx="22" cy="51" r="3"/><circle cx="33" cy="57" r="3"/><circle cx="44" cy="49" r="3"/></svg>
      <div class="tile__label">CURRICULUM<br><b>SUPPORT</b></div>
    </div>
    <div class="tile tile--hardware">
      <svg class="tile__icon" width="64" height="64" viewBox="0 0 64 64" fill="none" stroke="#fff" stroke-width="2.4"><rect x="16" y="16" width="32" height="32" rx="2"/><rect x="24" y="24" width="16" height="16"/><path d="M24 6v10M32 6v10M40 6v10M24 48v10M32 48v10M40 48v10M6 24h10M6 32h10M6 40h10M48 24h10M48 32h10M48 40h10"/></svg>
      <div class="tile__label">HARDWARE<br><b>SALES</b></div>
    </div>
    <div class="cover__title">
      <div class="title-light">SERVICE LEVEL</div>
      <div class="title-bold">AGREEMENT</div>
      <div class="ribbon">www.oru-lanex.example</div>
    </div>
  </div>
</section>

<!-- Back and front spread -->
<section class="section section--spread">
  <div class="spread">
    <div class="spread__page">
      <div class="back">
        <div class="back__strip" role="img" aria-label="Photo of a glowing teal circuit board"></div>
        <div class="back__info">
          <div class="brand-name"><span class="mark" style="width:10px;height:10px"></span>ORU LANEX</div>
          <div class="brand-tag">EDUCATION SUPPORT &amp; INSTALLATION</div>
          <div>Company No. 12345678</div>
          <div>Marlow Court,</div>
          <div>Fenwick street</div>
          <div>Dunhollow</div>
          <div>Westmere</div>
          <div>ZX4 7QN</div>
          <div class="contact-head">CONTACT US</div>
          <div>Email: hello@oru-lanex.example</div>
          <div>Telephone</div>
          <div>Office: 0100 555 0142</div>
          <div>Mobile: 0700 555 0193</div>
          <div>Web: www.oru-lanex.example</div>
        </div>
      </div>
    </div>
    <div class="spread__page">
      <div class="cover">
        <div class="cover__circuit" role="img" aria-label="Blue circuit board pattern with glowing hexagons"></div>
        <div class="cover__brand">
          <div class="brand-name"><span class="mark"></span>ORU LANEX</div>
          <div class="brand-tag">EDUCATION SUPPORT &amp; INSTALLATION</div>
        </div>
        <div class="tile tile--photo-desk" role="img" aria-label="Photo of a technician working on computer hardware"></div>
        <div class="tile tile--it">
          <svg class="tile__icon" width="62" height="62" viewBox="0 0 62 62" fill="none" stroke="#fff" stroke-width="2.4"><circle cx="31" cy="26" r="11"/><path d="M31 9v5M31 38v5M14 26h5M43 26h5M19 14l4 4M39 34l4 4M43 14l-4 4M23 34l-4 4"/><path d="M8 50c8-6 14-6 22-2h10c4 0 4 5 0 5H27M8 56h30l14-8"/></svg>
          <div class="tile__label">IT <b>SUPPORT</b></div>
        </div>
        <div class="tile tile--photo-board" role="img" aria-label="Close-up photo of a computer motherboard"></div>
        <div class="tile tile--curriculum">
          <svg class="tile__icon" width="66" height="62" viewBox="0 0 66 62" fill="none" stroke="#fff" stroke-width="2.4"><path d="M16 34a10 10 0 0 1 2-20 14 14 0 0 1 27 2 9 9 0 0 1 3 18z"/><path d="M22 34v14M33 34v20M44 34v12"/><circle cx="22" cy="51" r="3"/><circle cx="33" cy="57" r="3"/><circle cx="44" cy="49" r="3"/></svg>
          <div class="tile__label">CURRICULUM<br><b>SUPPORT</b></div>
        </div>
        <div class="tile tile--hardware">
          <svg class="tile__icon" width="64" height="64" viewBox="0 0 64 64" fill="none" stroke="#fff" stroke-width="2.4"><rect x="16" y="16" width="32" height="32" rx="2"/><rect x="24" y="24" width="16" height="16"/><path d="M24 6v10M32 6v10M40 6v10M24 48v10M32 48v10M40 48v10M6 24h10M6 32h10M6 40h10M48 24h10M48 32h10M48 40h10"/></svg>
          <div class="tile__label">HARDWARE<br><b>SALES</b></div>
        </div>
        <div class="cover__title">
          <div class="title-light">SERVICE LEVEL</div>
          <div class="title-bold">AGREEMENT</div>
          <div class="ribbon">www.oru-lanex.example</div>
        </div>
      </div>
    </div>
  </div>
</section>

<!-- Inside pages -->
<section class="section section--inside">
  <div class="inside">
    <article class="page page--left">
      <div class="page__note">All Prices Exclude VAT and are Valid for 10 Days only</div>
      <div class="cols cols--2">
        <div>
          <h2 class="h">ICT SLA 2018 <span>Coverage Level</span></h2>
          <ul class="ticks">
            <li>Weekly visits based on 39 weeks</li>
            <li>Extra support during Ofsted inspections (1 HR visit per inspection day)</li>
            <li>Email and telephone support</li>
            <li>Access to our tech support and logging portal</li>
          </ul>
        </div>
        <div>
          <ul class="ticks" style="margin-top:22px">
            <li>Unlimited break fix call out 08:00 - 16:00 Mon - Fri</li>
            <li>Remote access support for servers and all computers and laptops</li>
            <li>We do services call on the same day we log them</li>
          </ul>
        </div>
      </div>
      <h2 class="h">Equipment <span>Covered</span></h2>
      <p>Any hardware connected to the school ICT or admin network</p>
      <ul class="ticks cols">
        <li>Desktop PCs</li><li>Monitors</li><li>Servers and backup devices</li>
        <li>Digital cameras and video cameras</li><li>Interactive whiteboards and projectors</li><li>Printers</li>
        <li>Laptops</li><li>Tablets</li><li>Switches, routers and wireless equipment</li>
        <li>All cabling structures</li>
      </ul>
      <h2 class="h">Software and Online Services <span>Included in your SLA</span></h2>
      <ul class="ticks">
        <li>Antivirus management and monitoring software, with alerts sent each week in real time from any computer</li>
        <li>Cloud storage for all staff users</li>
        <li>School website hosting, domain name and email addresses included</li>
        <li>Remote device management system with safe web filtering</li>
      </ul>
      <h2 class="h">Staff Training and <span>Class Room Support</span></h2>
      <ul class="ticks">
        <li>We can provide training on any software package or online service in school</li>
        <li>All our technicians are aware that we need to provide staff support in class with ICT hardware and software</li>
      </ul>
      <h2 class="h">Contributions</h2>
      <p>Our team will support the school with planning for future ICT purchases and will give advice on new equipment, licences and upgrades so that budgets can be used in the best way each year.</p>
      <div class="page__foot"><span class="foot-brand">ORU LANEX</span><span class="foot-web">www.oru-lanex.example</span></div>
    </article>

    <article class="page page--right">
      <div class="page__note">All Prices Exclude VAT and are Valid for 10 Days only</div>
      <h2 class="h">After <span>School Clubs</span></h2>
      <p>We can run after school clubs for pupils, with one club per week per term. Clubs include coding, robotics and digital media, and are priced separately from the SLA.</p>
      <h2 class="h">Insurances, DBS <span>Checks and ID Badges</span></h2>
      <p>All our staff hold enhanced DBS checks and carry ID badges at all times. We hold full public liability and professional indemnity insurance, and copies are available on request.</p>
      <h2 class="h">Regular <span>Management Meetings</span></h2>
      <p>We meet with the head teacher or business manager each term to review support logs, plan upgrades and agree priorities for the next term.</p>
      <h2 class="h">Not Included <span>in the SLA</span></h2>
      <p>Repairs caused by misuse, new hardware, licences and third party services are not included and will be quoted separately before any work begins.</p>
      <h2 class="h">Termination <span>of Contract</span></h2>
      <p>Either party may end this agreement with one full term of written notice. Fees already paid for the current term are not refundable.</p>
      <h2 class="h">Prices and <span>Coverage Levels</span></h2>
      <div class="cols cols--2 price">
        <div>
          <p><b>1 x 3 hour visit every other week</b><br>£2,400 per annum payable termly</p>
          <ul class="ticks"><li>Autumn Term - £800</li><li>Spring Term - £800</li><li>Summer Term - £800</li></ul>
          <p style="margin-top:5px"><b>1 x 3 hour visit every week</b><br>£4,500 per annum payable termly</p>
          <ul class="ticks"><li>Autumn Term - £1,500</li><li>Spring Term - £1,500</li><li>Summer Term - £1,500</li></ul>
        </div>
        <div>
          <p><b>1 x 5 hour visit every week</b><br>£6,600 per annum payable termly</p>
          <ul class="ticks"><li>Autumn Term - £2,200</li><li>Spring Term - £2,200</li><li>Summer Term - £2,200</li></ul>
          <p style="margin-top:5px"><b>2 x 5 hour visit every week</b><br>£11,400 per annum payable termly</p>
          <ul class="ticks"><li>Autumn Term - £3,800</li><li>Spring Term - £3,800</li><li>Summer Term - £3,800</li></ul>
        </div>
      </div>
      <div class="page__foot"><span class="foot-brand">ORU LANEX</span><span class="foot-web">www.oru-lanex.example</span></div>
    </article>
  </div>
</section>

</body>
</html>
```